Granite Tile Retail Website

We need wireframe PSD for a website selling granite tile. There are 4 custom pages, shopping cart page, and checkout page. I have a logo designed but the color scheme is up to you.
Color Gallery - We have approximately 20 different stone colors. Each color will have a little gallery of its own pictures. On this page the customer can also add a sample piece of the color they are viewing to their shopping cart.
Questions Page - This page has 3 elements
1. Upload or fax diagram of kitchen for quotation
2. Installation video
3. Installation FAQ (text)
Order Page - This page has 3 steps for the customer
1. Customer chooses his color.
2. For each color we have numerous different products. He inputs the quantity of each product.
3. Customer is given total price and shipping quote. If order over $500 it says "This order qualifies for free shipping". Customer can click on button to "Order Now"
Shopping Cart - Very standard, just like I have attached here. Just modify for your colors / font.
Checkout - Just like in the attached. See design-explanation.docx for minor adjustments.
I have vector file for logo.
Please try to post your designs by tonightÂ
Home owners 40-60 years old
Shopping

```html
<!DOCTYPE html>
<html lang="en">
<head>
<meta charset="utf-8">
<title>Stonecrest – Granite Tile</title>
<link href="https://fonts.googleapis.com/css2?family=PT+Sans+Narrow:wght@700&family=Crimson+Text:wght@400&family=Arimo:wght@400;700&display=swap" rel="stylesheet">
<style>
:root{
  --teal:#5a958f;
  --teal-dark:#467b75;
  --teal-deep:#3b6a65;
  --body-grey:#e9e9e9;
  --text-grey:#8a8a8a;
  --white:#ffffff;
  --amber:#f6b400;
  --amber-light:#ffd740;
  --label-brown:#3a2410;
  --heading:#222222;
  --footer-link:#dff0ee;
}
*{margin:0;padding:0;box-sizing:border-box}
html,body{width:1200px;height:979px;overflow:hidden}
body{position:relative;background:#fff;font-family:'Arimo',Arial,sans-serif}
.abs{position:absolute}

.site-header{left:0;top:0;width:1200px;height:98px;background:linear-gradient(var(--teal-deep) 0 5px,var(--teal) 5px)}
.brand{left:240px;top:20px;display:flex;align-items:center;gap:10px}
.brand-square{width:30px;height:30px;background:var(--amber);border-radius:3px}
.brand-name{font-family:'Arimo',Arial,sans-serif;font-weight:700;font-size:30px;color:var(--white);letter-spacing:1px}
.cart-badge{left:866px;top:0;width:111px;height:31px;background:var(--teal-dark);border-radius:0 0 6px 6px;display:flex;align-items:center;gap:6px;padding-left:8px}
.cart-badge .dot{width:16px;height:16px;border-radius:50%;background:var(--amber)}
.cart-badge p{font-size:8px;line-height:10px;color:var(--amber-light)}
.main-nav{left:490px;top:62px;height:27px;display:flex;align-items:center}
.main-nav a{font-size:12px;font-weight:700;color:var(--white);text-decoration:none;text-transform:uppercase;margin-right:38px}
.main-nav a.active{background:linear-gradient(var(--amber-light),var(--amber));color:#5a3a00;padding:7px 18px;border-radius:5px;margin-right:26px}

.hero{left:0;top:98px;width:1200px;height:322px;background:linear-gradient(#dcdcdc,#f7f7f7 40%,#fbfbfb)}
.video{left:269px;top:168px;width:408px;height:230px;box-shadow:0 10px 14px -8px rgba(0,0,0,.35)}
.video-screen{width:408px;height:206px;background:linear-gradient(#6aa59f,#5a958f)}
.video-bar{width:408px;height:24px;background:linear-gradient(#f4f4f4,#cfcfcf)}
.hero-text{left:720px;top:161px;width:215px;font-size:9.6px;line-height:14.5px;color:var(--text-grey);text-align:justify}

.features{left:219px;top:420px;width:762px;height:188px;background:linear-gradient(#efefef,#fff)}
.tile{top:446px;width:212px;height:137px;border-radius:10px;background:radial-gradient(circle at 50% 35%,var(--amber-light),var(--amber) 75%);box-shadow:0 0 0 3px #fff,0 4px 8px rgba(0,0,0,.25);text-align:center}
.tile-label{position:absolute;left:0;right:0;bottom:10px;font-family:'PT Sans Narrow',sans-serif;font-weight:700;font-size:22px;color:var(--label-brown)}
.tile svg{margin-top:14px}

.welcome{left:228px;top:620px;font-family:'Crimson Text',serif;font-size:34px;color:var(--heading)}
.intro{left:228px;top:672px;width:744px;font-size:10.8px;line-height:16.6px;color:var(--text-grey);text-align:justify}

.footer-shade{left:0;top:830px;width:1200px;height:44px;background:linear-gradient(#fff,#dcdcdc)}
.site-footer{left:0;top:874px;width:1200px;height:105px;background:linear-gradient(var(--teal-dark) 0 3px,var(--teal) 3px)}
.footer-col{top:22px;list-style:none}
.footer-col li{font-size:10px;font-weight:700;color:var(--footer-link);line-height:24px}
.footer-col li::before{content:"→ ";font-weight:400;font-size:9px}
.footer-brand{right:223px;top:20px;display:flex;align-items:center;gap:6px}
.footer-brand .brand-square{width:16px;height:16px}
.footer-brand span{font-weight:700;font-size:16px;color:var(--white)}
.copyright{right:223px;top:70px;font-size:10.5px;line-height:15px;color:var(--white);text-align:right}
</style>
</head>
<body>

<header class="site-header abs">
  <div class="brand abs"><span class="brand-square"></span><span class="brand-name">STONECREST</span></div>
  <div class="cart-badge abs"><span class="dot"></span><p>Now in your cart<br>0 items</p></div>
  <nav class="main-nav abs">
    <a class="active" href="#">Home</a><a href="#">Gallery</a><a href="#">Questions</a><a href="#">Orderr</a><a href="#">Shopping Cart</a>
  </nav>
</header>

<section class="hero abs">
</section>
<div class="video abs">
  <div class="video-screen" role="img" aria-label="Installation video poster"></div>
  <svg class="abs" style="left:170px;top:70px" width="68" height="46" viewBox="0 0 68 46">
    <rect x="0" y="0" width="68" height="46" rx="6" fill="#1a1a1a" opacity=".85"/>
    <path d="M26 12 L46 23 L26 34Z" fill="#fff"/>
  </svg>
  <svg class="video-bar" width="408" height="24" viewBox="0 0 408 24">
    <path d="M8 7 L17 12 L8 17Z" fill="#333"/>
    <path d="M28 10h4l5-4v12l-5-4h-4z" fill="#333"/>
    <text x="50" y="15" font-size="8" fill="#444" font-family="Arial,sans-serif">0:00 / 3:05</text>
    <rect x="100" y="10" width="240" height="4" rx="2" fill="#9a9a9a"/>
    <circle cx="106" cy="12" r="5" fill="#555"/>
    <rect x="356" y="6" width="18" height="12" rx="2" fill="#555"/>
    <path d="M384 6h5M384 6v5M400 6h-5M400 6v5M384 18h5M384 18v-5M400 18h-5M400 18v-5" stroke="#333" stroke-width="2"/>
  </svg>
</div>
<p class="hero-text abs">Lorem Ipsum is simply dummy text of the printing and typesetting industry. Lorem Ipsum has been the industry's standard dummy text ever since the 1500s, when an unknown printer took a galley of type and scrambled it to make a type specimen book. It has survived not only five centuries, but also the leap into electronic typesetting, remaining essentially unchanged. It was popularised in the 1960s with the release of Letraset sheets containing orem Ipsum is simply dummy text of the printing and typesetting industry. Lorem Ipsum has been the</p>

<section class="features abs"></section>
<a class="tile abs" style="left:237px" href="#">
  <svg width="80" height="80" viewBox="0 0 80 80">
    <circle cx="40" cy="40" r="36" fill="#fff"/>
    <circle cx="40" cy="40" r="30" fill="#1f78c8"/>
    <text x="40" y="55" text-anchor="middle" font-size="42" font-weight="700" fill="#fff" font-family="Arial,sans-serif">?</text>
  </svg>
  <span class="tile-label">Questions?</span>
</a>
<a class="tile abs" style="left:490px" href="#">
  <div role="img" aria-label="Paint brush with colour splashes" style="width:80px;height:80px;margin:14px auto 0;border-radius:40px;background:radial-gradient(#3aa0d8,#e24f3a 60%,transparent 72%)"></div>
  <span class="tile-label">Color Selection</span>
</a>
<a class="tile abs" style="left:742px" href="#">
  <svg width="120" height="80" viewBox="0 0 120 80">
    <rect x="10" y="14" width="90" height="56" rx="4" fill="#3da3e0"/>
    <path d="M10 18 L55 48 L100 18" fill="none" stroke="#d6efff" stroke-width="3"/>
    <circle cx="94" cy="44" r="16" fill="#fff"/>
    <circle cx="94" cy="44" r="12" fill="#3da3e0"/>
    <path d="M100 44H88M93 38l-6 6 6 6" fill="none" stroke="#fff" stroke-width="3"/>
  </svg>
  <span class="tile-label">Get a Quote</span>
</a>

<h1 class="welcome abs">Welcome to Our Stonecrest!</h1>
<p class="intro abs">Lorem Ipsum is simply dummy text of the printing and typesetting industry. Lorem Ipsum has been the industry's standard dummy text ever since the 1500s, when an unknown printer took a galley of type and scrambled it to make a type specimen book. It has survived not only five centuries, but also the leap into electronic typesetting, remaining essentially unchanged. It was popularised in the 1960s with the release of Letraset sheets containing Lorem Ipsum is simply dummy text of the printing and typesetting industry. Lorem Ipsum has been the industry's standard dummy text ever since the 1500s, when an unknown printer took a galley of type and scrambled it to make a type specimen book. Lorem Ipsum is simply dummy text of the printing and typesetting industry. Lorem Ipsum has been the industry's standard dummy text ever since the 1500s, when an unknown printer took a galley of type and scrambled it to make a type specimen book. It has survived not only five centuries, but also the leap into electronic typesetting, remaining essentially unchanged. It was popularised in the 1960s with the release of Letraset sheets containing Lorem Ipsum is simply dummy text of the printing and typesetting industry.</p>

<div class="footer-shade abs"></div>
<footer class="site-footer abs">
  <ul class="footer-col abs" style="left:219px"><li>Home</li><li>Gallery</li><li>Questions</li></ul>
  <ul class="footer-col abs" style="left:331px"><li>Orderr</li><li>Shopping Cart</li><li>Contact Us</li></ul>
  <ul class="footer-col abs" style="left:466px"><li>Return Policy</li><li>Shipping Policy</li><li>Privacy</li></ul>
  <ul class="footer-col abs" style="left:591px"><li>Terms of Use</li><li>Customer Service</li></ul>
  <div class="footer-brand abs"><span class="brand-square"></span><span>STONECREST</span></div>
  <p class="copyright abs">© 2011 stonecrest.com.<br>All Rights Reserved</p>
</footer>

</body>
</html>
```